Business Card for Jewelry Business

We need a new namecard design for a jewelry company based in Bangkok, Thailand. We have a new website recently and want the new namecard to reflect our new modern image. I have uploaded our old namecard to show you the information that needs to be on the namecard. Pls check our website www.qelburn.com for the new color scheme to help design the new namecard.

```html
<!DOCTYPE html>
<html lang="en">
<head>
<meta charset="utf-8">
<title>Qelburn Business Card</title>
<link href="https://fonts.googleapis.com/css2?family=Jost:wght@400;500;600&family=Oswald:wght@400&display=swap" rel="stylesheet">
<style>
  :root {
    --backdrop: #ababab;
    --turquoise: #58cdd2;
    --charcoal: #1c2326;
    --map-tone: #242d30;
    --white: #ffffff;
    --soft-white: #e9ecec;
    --muted: #8b9193;
    --ring: #6b7375;
  }
  html, body {
    margin: 0;
    width: 1200px;
    height: 1000px;
    overflow: hidden;
    background: var(--backdrop);
    font-family: "Jost", sans-serif;
  }
  .canvas { position: relative; width: 1200px; height: 1000px; }
  .card {
    position: absolute;
    left: 294px;
    width: 613px;
    height: 352px;
    border-radius: 30px;
    overflow: hidden;
  }
  .card-front { top: 82px; background: var(--turquoise); }
  .card-back { top: 545px; background: var(--charcoal); }

  .front-badge {
    position: absolute;
    left: 231px; top: 100px;
    width: 152px; height: 152px;
    border-radius: 50%;
    background: var(--white);
    display: flex; align-items: center; justify-content: center;
  }
  .brand-name {
    font-family: "Jost", sans-serif;
    font-weight: 500;
    font-size: 26px;
    letter-spacing: 1px;
    color: var(--turquoise);
  }

  .world-map {
    position: absolute;
    left: 70px; top: 55px;
    width: 543px; height: 255px;
    background: radial-gradient(ellipse at 50% 45%, var(--map-tone) 0%, rgba(36,45,48,0.6) 55%, rgba(28,35,38,0) 80%);
  }

  .back-badge {
    position: absolute;
    left: 100px; top: 80px;
    width: 114px; height: 114px;
    border-radius: 50%;
    border: 1px solid var(--ring);
    display: flex; align-items: center; justify-content: center;
  }
  .back-badge .brand-name { color: var(--soft-white); font-size: 21px; }

  .tagline {
    position: absolute;
    left: 17px; top: 210px;
    width: 280px;
    margin: 0;
    text-align: center;
    font-size: 14.5px;
    line-height: 22px;
    text-transform: uppercase;
    color: var(--soft-white);
  }

  .contact-block { position: absolute; left: 339px; top: 86px; }
  .person-name {
    margin: 0;
    font-size: 25px;
    font-weight: 600;
    color: var(--turquoise);
    line-height: 30px;
  }
  .person-title {
    margin: 4px 0 0;
    font-family: "Oswald", sans-serif;
    font-size: 9.5px;
    letter-spacing: 1.3px;
    text-transform: uppercase;
    color: var(--muted);
  }
  .contact-list { list-style: none; margin: 28px 0 0; padding: 0; }
  .contact-item {
    position: relative;
    padding-left: 30px;
    font-size: 13.5px;
    line-height: 26.5px;
    color: var(--muted);
  }
  .contact-item.email { color: var(--soft-white); }
  .contact-icon { position: absolute; left: 0; top: 6px; width: 15px; height: 15px; }
</style>
</head>
<body>
<div class="canvas">
  <section class="card card-front">
    <div class="front-badge"><span class="brand-name">Qelburn</span></div>
  </section>

  <section class="card card-back">
    <div class="world-map" role="img" aria-label="Faint world map backdrop"></div>

    <div class="back-badge"><span class="brand-name">Qelburn</span></div>
    <p class="tagline">Manufacturers of fine gold &amp; silver jewelry</p>

    <div class="contact-block">
      <h1 class="person-name">Nalin Sukprasert</h1>
      <p class="person-title">Sales &amp; Product Development Manager</p>
      <ul class="contact-list">
        <li class="contact-item">
          <svg class="contact-icon" viewBox="0 0 24 24"><path d="M6.6 10.8a15 15 0 0 0 6.6 6.6l2.2-2.2a1 1 0 0 1 1-.25 11.4 11.4 0 0 0 3.6.6 1 1 0 0 1 1 1V20a1 1 0 0 1-1 1A17 17 0 0 1 3 4a1 1 0 0 1 1-1h3.5a1 1 0 0 1 1 1c0 1.25.2 2.45.6 3.6a1 1 0 0 1-.25 1z" fill="none" stroke="#58cdd2" stroke-width="2"/></svg>
          +662-418-0736
        </li>
        <li class="contact-item">
          <svg class="contact-icon" viewBox="0 0 24 24"><path d="M12 2a7 7 0 0 0-7 7c0 5 7 13 7 13s7-8 7-13a7 7 0 0 0-7-7zm0 9.5A2.5 2.5 0 1 1 12 6.5a2.5 2.5 0 0 1 0 5z" fill="#58cdd2"/></svg>
          128 Moo 7 Rattanathibet Road,<br>Bang Phli Industrial Estate,<br>Bangkok, 10540 Thailand
        </li>
        <li class="contact-item email">
          <svg class="contact-icon" viewBox="0 0 24 24" style="width:18px;height:18px;left:-2px;top:5px"><text x="12" y="18" text-anchor="middle" font-family="Jost, sans-serif" font-size="21" font-weight="600" fill="#58cdd2">@</text></svg>
          hello@qelburn.com
        </li>
      </ul>
    </div>
  </section>
</div>
</body>
</html>
```